Influencer Marketing Präsentation
Zielgruppe
Ich: Influencer
Anlass: Weiterbildungs-Tagung
Zielgruppe: Teilnehmer der Digital Marketing-Weiterbildung, welche zeitgleich auch Marketing-Leute sind von Unternehmen, die etwas über Influencer Marketing erfahren möchten.
Aufgabenstellung
Ich benötige eine pfannenfertige PPTX Präsentation für meinen Vortrag an einer Digital-Marketing Tagung!
Die Präsentation ist 20min maximal, plus 10min Q&A. Sie soll cool daherkommen, aber nicht zu verspielt. Die Leute sollen sich auch denken 'wow, der hat nicht nur was als Influencer auf dem Kasten, sondern hat auch eine coole PPT zu seinem Vortrag!' Da den ganzen Tag lang unterschiedliche Leute präsentieren zu verschiedensten Marketing Themen, will ich die Präsentation locker und cool gestalten und nicht zu heftig mit Zahlen und schwerem Inhalt.
Die angehängte PPT ist ein Mix aus zwei 'alten' Präsentationen, welche ich zu dem Thema gemacht habe. Nun gilt es, die coolsten Themen rauszupicken, diese bei Bedarf auf Deutsch zu übersetzen, und allenfalls noch andere Influencer-Marketing Themen, Tips & tricks einzubauen.
Im ersten Slide der angehängten Präsentation siehst Du ein Inhaltsverzeichnis. so stelle ich mir das in etwa vor. bin aber auch offen, das ganze zu straffen!
Hier noch ein Link zu einer online verfügbaren Präsentation, von welcher ich folgende Slides integrieren möchte (anders darstellen und Umtexten bitte, damit man nicht 1:1 kopiert!) https://folienkiste.example/slide/48213907/
Slides: 5, 6, 7, 8, 11. Können auch zusammengefasst werden auf 2-3 slides!
Das fertige Projekt (Präsentation) sollte im PPTX Format angeliefert werden, so dass ich allenfalls noch letzte inhaltliche Korrekturen anbringen kann.

```html
<!DOCTYPE html>
<html lang="de">
<head>
<meta charset="utf-8">
<title>Influencer Marketing – Vergütungsmodelle und Ziele</title>
<link rel="stylesheet" href="https://fonts.googleapis.com/css2?family=Old+Standard+TT:wght@400&display=swap">
<style>
  :root {
    --slide-bg: #ffffff;
    --ink: #1a1a1a;
    --divider: #b5b5b5;
    --sky-top: #4fa4ad;
    --sky-mid: #a9cfd6;
    --sky-light: #d8e8ea;
    --mountain: #6f8a80;
    --forest: #2f4a3c;
    --shade: #1c2421;
  }
  * { margin: 0; padding: 0; box-sizing: border-box; }
  html, body {
    width: 1200px;
    height: 674px;
    overflow: hidden;
    background: var(--slide-bg);
  }
  .slide {
    position: relative;
    width: 1200px;
    height: 674px;
    background: var(--slide-bg);
    font-family: "Old Standard TT", "Times New Roman", serif;
    color: var(--ink);
  }
  .hero-photo {
    position: absolute;
    left: 0;
    top: 0;
    width: 536px;
    height: 674px;
    clip-path: polygon(0 0, 430px 0, 536px 214px, 536px 674px, 0 674px);
    background:
      linear-gradient(180deg,
        var(--sky-top) 0%,
        var(--sky-mid) 28%,
        var(--sky-light) 42%,
        var(--mountain) 58%,
        var(--forest) 78%,
        var(--shade) 100%);
  }
  .divider-line {
    position: absolute;
    left: 0;
    top: 0;
  }
  .label {
    position: absolute;
    transform: translateX(-50%);
    text-align: center;
    text-transform: uppercase;
    font-size: 21px;
    line-height: 32px;
    letter-spacing: 0.5px;
    white-space: nowrap;
  }
  .label--model { top: 33px; }
  .label--goal-row1 { top: 310px; }
  .label--goal-row2 { top: 486px; }
</style>
</head>
<body>
  <main class="slide">
    <div class="hero-photo" role="img" aria-label="Foto: Vater trägt seine kleine Tochter auf dem Arm, von hinten gesehen, vor Berggipfel und Holzhütte unter blauem Himmel"></div>

    <svg class="divider-line" width="1200" height="674" viewBox="0 0 1200 674" aria-hidden="true">
      <line x1="724" y1="0" x2="582" y2="277" stroke="var(--divider)" stroke-width="1.5"/>
    </svg>

    <div class="label label--model" style="left:127px">Bezahlung<br>pro Post/<br>Video</div>
    <div class="label label--model" style="left:327px">Kostenlose<br>Produkte /<br>Erlebnisse</div>
    <div class="label label--model" style="left:571px">Bezahlung<br>auf Basis<br>Anzahl<br>Likes</div>
    <div class="label label--model" style="left:801px">Bezahlung<br>auf Basis<br>Anzahl Clicks</div>
    <div class="label label--model" style="left:1036px">Bezahlung<br>nach Anzahl<br>Verkäufe</div>

    <div class="label label--goal-row1" style="left:755px">Steigerung<br>der<br>Aufmerksamkeit</div>
    <div class="label label--goal-row1" style="left:993px">Interaktionen<br>mit Community<br>steigern</div>

    <div class="label label--goal-row2" style="left:755px">Präsenz<br>verbessern</div>
    <div class="label label--goal-row2" style="left:993px">Follower Daten<br>sammeln</div>
  </main>
</body>
</html>
```